Facebook Ads for Leading Telemedicine Provider

Need a variation of this advertisement.

Would like to leave everything the same with white as the dominant color but test the pink circle with a different design style

Target Market(s)

Male / Female from 18-65

Industry/Entity Type

Health

Requirements
Must have
• Use the image attached and test a different background

```html
<!DOCTYPE html>
<html lang="en">
<head>
<meta charset="UTF-8">
<title>Wellvo – Free Covid Testing at Home</title>
<link href="https://fonts.googleapis.com/css2?family=Open+Sans:wght@600;700;800&display=swap" rel="stylesheet">
<style>
  :root {
    --white: #ffffff;
    --navy: #0e1f5b;
    --ink: #1b2a4a;
    --shield-rim: #c4dcf5;
    --shield-tint: #eaf2fc;
    --cross: #8fb9e6;
    --virus-light: #ffb347;
    --virus-mid: #ff9a1f;
    --virus-deep: #f26a0c;
    --scene-light: #f3f6fb;
    --scene-mid: #e7ddc8;
  }
  html, body {
    margin: 0;
    padding: 0;
    width: 1200px;
    height: 1200px;
    overflow: hidden;
    background: var(--white);
  }
  .ad {
    position: relative;
    width: 1200px;
    height: 1200px;
    overflow: hidden;
    background: var(--white);
    font-family: "Open Sans", Arial, sans-serif;
  }
  .virus {
    position: absolute;
    border-radius: 50%;
    background: radial-gradient(circle at 40% 38%, var(--virus-light), var(--virus-mid) 55%, var(--virus-deep));
  }
  .virus--corner { left: 0; top: -70px; width: 320px; height: 320px; }
  .virus--top-right { left: 640px; top: -30px; width: 500px; height: 500px; }
  .virus--left { left: -230px; top: 300px; width: 420px; height: 420px; }
  .virus--bottom-left { left: 30px; top: 860px; width: 330px; height: 330px; }

  .brand {
    position: absolute;
    left: 100px;
    top: 86px;
    margin: 0;
    font-size: 58px;
    font-weight: 700;
    color: var(--white);
    letter-spacing: -1px;
    line-height: 1;
  }
  .shield {
    position: absolute;
    left: 0;
    top: 0;
    width: 1200px;
    height: 1200px;
  }
  .headline {
    position: absolute;
    left: 0;
    top: 236px;
    width: 826px;
    margin: 0;
    text-align: center;
    font-size: 126px;
    font-weight: 700;
    line-height: 148px;
    letter-spacing: -3px;
    color: var(--navy);
  }
  .cta {
    position: absolute;
    left: 174px;
    top: 772px;
    width: 422px;
    height: 98px;
    border-radius: 6px;
    background: var(--navy);
    color: var(--white);
    font-size: 36px;
    font-weight: 700;
    display: flex;
    align-items: center;
    justify-content: center;
    text-decoration: none;
  }
  .scene {
    position: absolute;
    left: 620px;
    top: 520px;
    width: 580px;
    height: 610px;
    border-radius: 24px;
    background: linear-gradient(160deg, var(--scene-light), var(--scene-mid));
  }
  .url {
    position: absolute;
    left: 171px;
    top: 1124px;
    margin: 0;
    font-size: 29px;
    font-weight: 600;
    color: var(--ink);
  }
</style>
</head>
<body>
<main class="ad">
  <div class="virus virus--corner" role="img" aria-label="Orange virus illustration"></div>
  <div class="virus virus--top-right" role="img" aria-label="Large orange virus illustration"></div>
  <div class="virus virus--left" role="img" aria-label="Orange virus illustration"></div>
  <div class="virus virus--bottom-left" role="img" aria-label="Orange virus illustration"></div>

  <svg class="shield" viewBox="0 0 1200 1200" aria-hidden="true">
    <defs>
      <clipPath id="shield-inner">
        <path d="M0 218 Q410 92 818 218 L818 640 Q790 920 405 1092 Q60 920 8 640 Z"/>
      </clipPath>
    </defs>
    <path d="M0 218 Q410 92 818 218 L818 640 Q790 920 405 1092 Q60 920 8 640 Z"
          fill="var(--white)" stroke="var(--shield-rim)" stroke-width="24" stroke-linejoin="round"/>
    <g clip-path="url(#shield-inner)">
      <rect x="0" y="0" width="405" height="1200" fill="var(--shield-tint)"/>
      <rect x="222" y="240" width="114" height="360" fill="var(--cross)" opacity="0.55"/>
      <rect x="90" y="360" width="470" height="112" fill="var(--cross)" opacity="0.55"/>
    </g>
  </svg>

  <p class="brand">Wellvo</p>

  <h1 class="headline">Free Covid<br>Testing at<br>Home</h1>
  <a class="cta" href="#">BOOK NOW</a>

  <div class="scene" role="img" aria-label="Illustration of a woman opening her front door to a masked health worker holding a clipboard, with a plant, welcome mat and virus-free and check icons"></div>

  <p class="url">https://wellvo.org/covid-testing</p>
</main>
</body>
</html>
```